TORNAVE5 Research Outcomes (e-Toolkit)

I would like you to design an electronic document that can be used to display the outcomes of the TORNAVE5 Research that can easily be downloaded from a website. This document will help nurses, educators, students and their supervisors to be able to better understand the outcomes of the research and apply it to their own practice. It should be something they can print out (A4 size) and refer to easily. It should be quite graphical and represent male and female nurses working in different specialty areas (emergency, primary healthcare, aged care, etc.), across hospital to primary healthcare (community) contexts. It should be professional, clean and crisp in appearance. There are areas in yellow in the attached document that are yet to be determined. All images within the document can be amended to better reflect the design of the document and the intent of its contained content. An example of the type of document I'm looking for is attached as "standards.pdf". It should be approximately 15 pages in length.
Updates

The project does not have to use the TORNAVE5 logo or its colours as a main design feature of the project.

Target Market(s)

Nurses, educators and students.

Industry/Entity Type

Education

Font styles to use
Sans Serif

Colors

Designer to choose colors to be used in the design.

Requirements
Must have
• Must have a diagram depicting the interrelatedness of all the individual metaspecialties. The contained diagrams can be modified to suit graphic design needs.
• Images of nursing professionals should appear Australian.
Nice to have
• I would like them to try and re-configure the diagrams as they are boring and I hate the colours. Images of collaboration amongst different healthcare team members would be nice.
Should not have
• Only images of female nurses or only images (if chosen) of nurses only working in a hospital.

```html
<!DOCTYPE html>
<html lang="en">
<head>
<meta charset="utf-8">
<title>Metaspecialties – Suggested Application and Exemplar</title>
<link rel="stylesheet" href="https://fonts.googleapis.com/css2?family=Quicksand:wght@400;500;600;700&display=swap">
<style>
  :root {
    --paper: #fbfbfb;
    --ink: #6b6b6b;
    --ink-dark: #3f3f3f;
    --teal: #5cc3b2;
    --teal-deep: #2ba691;
    --teal-light: #8ed8cb;
    --teal-pale: #d6f1ec;
    --edge: #e47d3e;
    --rule: #2f4f4a;
  }
  * { box-sizing: border-box; margin: 0; padding: 0; }
  html, body { width: 1200px; height: 756px; overflow: hidden; background: #ececea; }
  body { font-family: "Quicksand", sans-serif; color: var(--ink); }

  .spread { position: relative; width: 1200px; height: 756px; display: flex; }
  .page { position: relative; width: 600px; height: 756px; background: var(--paper); }
  .page--left { box-shadow: inset -30px 0 40px -30px rgba(0,0,0,.18); }
  .page--right { box-shadow: inset 30px 0 40px -30px rgba(0,0,0,.18); }
  .page-edge { position: absolute; top: 0; width: 6px; height: 100%; background: var(--edge); }
  .page--left .page-edge { left: 0; }
  .page--right .page-edge { right: 0; }

  .pattern { position: absolute; top: 0; }
  .page--left .pattern { left: 66px; width: 510px; height: 180px;
    background: linear-gradient(200deg, var(--teal-light) 0%, var(--teal-pale) 55%, rgba(214,241,236,0) 100%);
    clip-path: polygon(0 0, 100% 0, 100% 70%, 70% 100%, 55% 95%, 20% 50%); }
  .page--right .pattern { left: 0; width: 518px; height: 160px;
    background: linear-gradient(160deg, var(--teal-light) 0%, var(--teal-pale) 55%, rgba(214,241,236,0) 100%);
    clip-path: polygon(0 0, 100% 0, 80% 45%, 45% 100%, 25% 90%, 0 40%); }

  .body-text { position: absolute; font-size: 12.2px; line-height: 19px; color: var(--ink); }
  .intro { left: 147px; top: 170px; width: 222px; }
  .col-one { left: 91px; top: 161px; width: 206px; }
  .col-two { left: 304px; top: 161px; width: 206px; }

  .section-title { position: absolute; left: 166px; top: 356px; font-size: 18px; font-weight: 500; color: #5a5a5a; }
  .section-title strong { font-weight: 600; }

  .role-label { position: absolute; top: 406px; width: 160px; text-align: center; font-size: 12px; line-height: 19px; }
  .role-label--aged { left: 134px; }
  .role-label--ed { left: 372px; }

  .meta-circle { position: absolute; top: 446px; width: 110px; height: 110px; border-radius: 50%;
    background: radial-gradient(circle at 40% 35%, #78d3c4, var(--teal-deep));
    display: flex; align-items: center; justify-content: center; text-align: center;
    color: #fff; font-size: 9px; line-height: 10px; font-weight: 500; }
  .meta-circle--aged { left: 159px; }
  .meta-circle--ed { left: 397px; }

  .meta-box { position: absolute; width: 139px; height: 43px; background: linear-gradient(90deg, var(--teal), var(--teal-deep));
    display: flex; align-items: center; justify-content: center; color: #fff; font-size: 9px; font-weight: 500; }
  .col-a { left: 144px; } .col-b { left: 382px; }
  .row-1 { top: 566px; } .row-2 { top: 625px; }

  .caption { position: absolute; font-size: 7.2px; line-height: 9px; color: var(--ink); }
  .caption strong { color: var(--ink-dark); }
  .caption--left { left: 144px; top: 716px; width: 380px; }
  .caption--right { left: 91px; top: 722px; width: 420px; }

  .folio { position: absolute; top: 734px; font-size: 8px; color: var(--ink-dark); }
  .page--left .folio { left: 572px; }
  .page--right .folio { left: 33px; }

  .exemplar-title { position: absolute; left: 91px; width: 414px; top: 462px; text-align: center; font-size: 18px; font-weight: 500; color: var(--ink-dark); }
  .cell { position: absolute; border: 1.2px solid var(--rule); background: var(--teal);
    display: flex; align-items: center; justify-content: center; text-align: center; color: #2d4f49; }
  .cell--role { left: 91px; top: 491px; width: 414px; height: 24px; font-size: 8.5px; color: #e9fbf7; }
  .cell--meta { top: 523px; height: 35px; font-size: 8.5px; line-height: 9px; color: #eefcf9; }
  .cell--standard { top: 563px; width: 129px; height: 123px; padding: 4px 6px; font-size: 7px; line-height: 7.8px; background: var(--teal-light); }
  .m-child { left: 91px; width: 129px; } .m-emerg { left: 233px; width: 272px; }
  .s-1 { left: 91px; } .s-2 { left: 233px; } .s-3 { left: 376px; }
  .key-activities { position: absolute; top: 694px; width: 129px; text-align: center; font-size: 8px; color: var(--ink-dark); }
</style>
</head>
<body>
<main class="spread">
  <section class="page page--left">
    <div class="page-edge"></div>
    <div class="pattern" role="img" aria-label="Decorative cluster of teal triangles"></div>

    <p class="body-text intro">Figure 3 provides two examples of how the mental health metaspecialty might be relevant both to a nurse practitioner based in an aged care facility and a nurse practitioner specialising in adolescent mental health care in an emergency department.</p>

    <h2 class="section-title">Suggested Application of the meta<strong>specialties</strong></h2>

    <p class="role-label role-label--aged">Eg: NP In Aged Care Facility</p>
    <p class="role-label role-label--ed">Eg: NP In Emergency Department</p>

    <div class="meta-circle meta-circle--aged">Aging &amp;<br>Palliative Care</div>
    <div class="meta-circle meta-circle--ed">Emergency &amp;<br>Acute Care</div>

    <div class="meta-box col-a row-1">Chronic &amp; Complex Care</div>
    <div class="meta-box col-a row-2">Mental Health Care</div>
    <div class="meta-box col-b row-1">Child &amp; Family Health Care</div>
    <div class="meta-box col-b row-2">Mental Health Care</div>

    <p class="caption caption--left"><strong>Figure 3:</strong> Suggested application of three complimentary metaspecialties for two nurse practitioner roles, namely aged care and emergency roles.</p>
    <span class="folio">5</span>
  </section>

  <section class="page page--right">
    <div class="page-edge"></div>
    <div class="pattern" role="img" aria-label="Decorative cluster of teal triangles"></div>

    <p class="body-text col-one">The metaspecialties are intended to compliment each other, rather than be applied as mutually exclusive constructs. Nurse practitioners, depending on their clinical practice scope, may draw standards from one or more metaspecialties. For example, a nurse practitioner working in a paediatric emergency department may draw standards from both child and family care and from emergency and acute care. The exemplar below (see Figure 2) demonstrates this concept. The top row (blue) indicates the</p>
    <p class="body-text col-two">title of the nurse practitioner role. The second row (red) indicates two metaspecialty titles and the third row (green) provides an example of one standard from the child and family care metaspecialty and two from the emergency and acute care specialty. Key activities, consistent with the ‘practice activities’ identified by Marlowe (2015), can be developed to provide specific structure to learning objectives and to acknowledge the local practice context and specific learning needs.</p>

    <h2 class="exemplar-title">Exemplar</h2>
    <div class="cell cell--role">Paediatric emergency NP</div>
    <div class="cell cell--meta m-child">Child and<br>family care</div>
    <div class="cell cell--meta m-emerg">Emergency and<br>acute care</div>
    <div class="cell cell--standard s-1">Demonstrates advanced understanding of variation in physiology and pathophysiology, particularly related to neonatal, paediatric and adolescent milestones</div>
    <div class="cell cell--standard s-2">Recognises and appropriately manages subtle and/or rapid changes in status of acutely and critically ill persons to promote stabilisation and prevent deterioration where possible</div>
    <div class="cell cell--standard s-3">Demonstrates ability to address complex health issues and provide comprehensive, individualised health education including life threatening conditions where there are linguistic, literacy, comprehension or other barriers to understanding</div>
    <p class="key-activities s-1">Key Activities ....</p>
    <p class="key-activities s-2">Key Activities ....</p>
    <p class="key-activities s-3">Key Activities ....</p>

    <p class="caption caption--right"><strong>Figure 2:</strong> Exemplar of metaspecialties and standards specific to a paediatric emergency nurse practitioner</p>
    <span class="folio">4</span>
  </section>
</main>
</body>
</html>
```